Frostwyn.co - Polar Expeditions Specialists

We need a modern, visually striking business card for Frostwyn.co, a company specialized in selling expedition cruises to the most remote regions on Earth, with a focus on the Arctic and Antarctica. The design should instantly communicate that the cardholder is an expert in polar travel. Use clean, premium aesthetics with cool tones like icy blue and white, possibly incorporating polar imagery (ice, glaciers, penguins, etc.)

Attached the logo

Contact Information for Business Card

Feels high-end and trustworthy.. Visually memorable — encourages people to keep it

Colors
0054AA
0677BA
7BADD7
CADEEF
E8F1F8

Requirements
Must have
• ice, glaciers, penguins, montains
Nice to have
• modern, transparente,

```html
<!DOCTYPE html>
<html lang="en">
<head>
<meta charset="utf-8">
<title>Frostwyn.co – Business Card</title>
<link href="https://fonts.googleapis.com/css2?family=Poppins:wght@500;600&family=Inter:wght@400;500;600&display=swap" rel="stylesheet">
<style>
  :root {
    --backdrop: #7a7a7a;
    --card-front: #100e28;
    --card-back-top: #262640;
    --card-back-mid: #1b2440;
    --card-back-low: #1e2a48;
    --ink: #ffffff;
    --ink-soft: #f2f6fb;
    --ink-muted: #8d93a8;
    --rule: rgba(255,255,255,0.22);
    --shadow: rgba(0,0,0,0.35);
  }
  * { margin: 0; padding: 0; box-sizing: border-box; }
  html, body {
    width: 1200px; height: 1200px; overflow: hidden;
    background: var(--backdrop);
  }
  .sheet { position: relative; width: 1200px; height: 1200px; }
  .card {
    position: absolute; left: 180px; width: 867px; height: 498px;
    box-shadow: 0 14px 30px var(--shadow);
    overflow: hidden;
  }
  .card--front { top: 85px; background: var(--card-front); }
  .card--back { top: 625px; }
  .card__scenery {
    position: absolute; inset: 0;
    background:
      radial-gradient(ellipse at 25% 70%, rgba(70,80,120,0.35), transparent 60%),
      linear-gradient(180deg, var(--card-back-top) 0%, var(--card-back-mid) 45%, var(--card-back-low) 100%);
  }
  .brand { position: absolute; display: flex; align-items: center; white-space: nowrap; }
  .brand__dot { border-radius: 50%; background: var(--ink-soft); flex: none; }
  .brand__name {
    font-family: 'Poppins', sans-serif; font-weight: 600; color: var(--ink-soft);
    line-height: 1; display: block;
  }
  .brand__tagline {
    font-family: 'Poppins', sans-serif; font-weight: 500; color: var(--ink-soft);
    line-height: 1; display: block;
  }
  .card--front .brand { left: 200px; top: 195px; }
  .card--front .brand__dot { width: 84px; height: 84px; margin-right: 42px; }
  .card--front .brand__name { font-size: 50px; }
  .card--front .brand__tagline { font-size: 16px; margin-top: 10px; }
  .card--back .brand { left: 122px; top: 196px; }
  .card--back .brand__dot { width: 62px; height: 62px; margin-right: 32px; }
  .card--back .brand__name { font-size: 36px; }
  .card--back .brand__tagline { font-size: 13px; margin-top: 8px; }
  .contact {
    position: absolute; left: 463px; top: 109px; height: 248px;
    border-left: 1px solid var(--rule); padding-left: 20px;
    font-family: 'Inter', sans-serif; color: var(--ink);
  }
  .contact__name { font-size: 27px; font-weight: 600; letter-spacing: 1.5px; line-height: 1; margin-top: 10px; }
  .contact__title { font-size: 19px; color: var(--ink-muted); letter-spacing: 1px; margin-top: 6px; }
  .contact__address { font-size: 19px; letter-spacing: 3px; line-height: 35px; margin-top: 12px; }
  .contact__list { list-style: none; margin-top: 7px; }
  .contact__item { display: flex; align-items: center; font-size: 20px; letter-spacing: 3px; height: 32px; }
  .contact__icon { width: 22px; height: 22px; margin-right: 12px; flex: none; }
</style>
</head>
<body>
<main class="sheet">
  <section class="card card--front">
    <div class="brand">
      <span class="brand__dot"></span>
      <div>
        <span class="brand__name">Frostwyn.co</span>
        <span class="brand__tagline">Polar Expeditions Specialists</span>
      </div>
    </div>
  </section>

  <section class="card card--back">
    <div class="card__scenery" role="img" aria-label="Dimmed photograph of glaciers and snowy mountain peaks under a dusky sky"></div>
    <div class="brand">
      <span class="brand__dot"></span>
      <div>
        <span class="brand__name">Frostwyn.co</span>
        <span class="brand__tagline">Polar Expeditions Specialists</span>
      </div>
    </div>
    <div class="contact">
      <h1 class="contact__name">MARCUS HALE</h1>
      <p class="contact__title">President/Owner</p>
      <p class="contact__address">48 Harbor Lane<br>Northport, ME 04849</p>
      <ul class="contact__list">
        <li class="contact__item">
          <svg class="contact__icon" viewBox="0 0 24 24" fill="none" stroke="#fff" stroke-width="2" stroke-linecap="round">
            <path d="M7 3h3l1 5-2 1.5c1 2.2 2.3 3.5 4.5 4.5L15 12l5 1v3a2 2 0 0 1-2 2C10 18 4 12 4 5a2 2 0 0 1 2-2z" transform="translate(-1 2) scale(0.85)"/>
            <path d="M16 7a3 3 0 0 1 0 5M19 5a6 6 0 0 1 0 9"/>
          </svg>
          207-555-0142
        </li>
        <li class="contact__item">
          <svg class="contact__icon" viewBox="0 0 24 24" fill="#fff">
            <path d="M2 7h20v11H2z"/><path d="M2 7l10 7 10-7" fill="none" stroke="#1b2440" stroke-width="1.6"/>
          </svg>
          marcus@frostwyn.co
        </li>
        <li class="contact__item">
          <svg class="contact__icon" viewBox="0 0 24 24" fill="none" stroke="#fff" stroke-width="2">
            <circle cx="12" cy="12" r="9.5"/>
            <path d="M5 8c3 0 3 3 5 3s1 4 3 5M14 3c0 3 4 2 4 5s3 2 3 3" stroke-width="1.8"/>
          </svg>
          frostwyn.co
        </li>
      </ul>
    </div>
  </section>
</main>
</body>
</html>
```